Review/Re-Design Supermarket E-Commerce website

We have launched our Supermarket E-commerce Website but feel it is lacking a modern feel.

Please re-design the current Supermarket E-commerce site, creating a more modern look and feel.

I am looking for design changes to things such as:

- Fonts
- Button shape & Size
- Shapes of boxes
- Layout of drop down menus
- A new shopping cart / button
- The Header (and in particular the use and positioning of the logo)
- Supplying a generic background image (currently berries)

Please do not change the structure of the page. For instance, the category selection will always be on the left, the items will always be displayed in rows of 3 and the shopping cart should be on the right.
Updates

Current site can be found at www.brovanmarket.com.au

Project Deadline Extended
Reason: designs coming in are generally too different from current design. we are looking for less that 10% change to the overall look and feel. one aspect that needs a lot of work is the checkout cart on the right hand side. please checkout http://www2.pelkinfreshmart.com.au/?gclid=QXRP4kdmwnLBHTYEzJuaPGEKtB

Target Market(s)

Consumers buying their weekly grocery shopping online

Industry/Entity Type

Shopping

Number of Pages Required

1 page

Requirements
Must have
• Stick to the branding of the Logo. Which is Red, Blue and White.
• Other colours may be used in small percentages.
Should not have
• Do not change the Structure of the site.

```html
<!DOCTYPE html>
<html lang="en">
<head>
<meta charset="utf-8">
<title>Brovan Market – Featured Products</title>
<link rel="stylesheet" href="https://fonts.googleapis.com/css2?family=Dosis:wght@500;600&family=Roboto:wght@400;500;700;900&display=swap">
<style>
:root{
  --red:#e8192c;
  --red-dark:#c8101f;
  --blue:#1c5aa8;
  --ink:#222;
  --grey:#555;
  --charcoal:#3b3b3b;
  --line:#cfcfcf;
  --topbar:#f6f6f6;
  --footer:#f0efed;
  --backdrop:#e4e4e4;
  --white:#fff;
}
*{box-sizing:border-box;margin:0;padding:0}
html,body{width:1127px;height:1200px;overflow:hidden}
body{background:var(--backdrop);font-family:"Roboto",Arial,sans-serif;color:var(--ink)}
.stage{position:absolute;left:0;top:0;width:1409px;height:1500px;transform:scale(.8);transform-origin:0 0}
.page{position:absolute;left:283px;top:0;width:844px;height:1456px;background:var(--white)}
.abs{position:absolute}

.topbar{left:0;top:0;width:844px;height:33px;background:var(--topbar);font-family:"Dosis",sans-serif;font-weight:600;font-size:11px;color:#333}
.topbar .phone{left:42px;top:10px;display:flex;align-items:center;gap:4px}
.topbar nav{right:48px;top:10px;display:flex;gap:19px}

.header{left:0;top:33px;width:844px;height:97px;box-shadow:0 2px 3px rgba(0,0,0,.05)}
.brand{left:42px;top:35px;display:flex;align-items:center;gap:8px;font-weight:900;font-size:21px;color:var(--blue);letter-spacing:.3px}
.brand .dot{width:14px;height:14px;border-radius:50%;background:var(--red)}
.search{left:302px;top:35px;display:flex}
.search input{width:147px;height:23px;border:1px solid #ddd;font:11px "Roboto",sans-serif;padding-left:8px;color:#999}
.search button{width:34px;height:23px;background:var(--red);border:0;display:flex;align-items:center;justify-content:center}
.cart{left:689px;top:27px;display:flex;align-items:center;gap:8px;font-size:11px;color:#444}

.cats{left:42px;top:153px;width:155px;height:352px;background:var(--red);border-radius:4px 4px 6px 6px;overflow:hidden}
.cats h2{height:33px;background:var(--charcoal);color:#eee;font-size:15px;font-weight:500;padding:8px 0 0 27px;letter-spacing:.2px}
.cats li{list-style:none;height:22px;border-bottom:1px solid #c90f1f;color:var(--white);font-size:11px;padding:5px 0 0 27px}
.cats li.active{background:var(--charcoal);border-color:#2c2c2c}

.banner{left:211px;top:153px;width:590px;height:230px;border-radius:6px;overflow:hidden;
  background:linear-gradient(90deg,#201810 0%,#2c2416 40%,#4a3a1e 60%,#3b4a20 75%,#6a3a18 100%)}
.banner .shade{position:absolute;inset:0;background:radial-gradient(circle at 80% 35%,rgba(170,160,130,.45),transparent 45%),radial-gradient(circle at 70% 85%,rgba(190,70,30,.5),transparent 40%)}
.banner .copy{position:absolute;left:26px;top:26px;width:320px;color:var(--white)}
.banner h1{font-size:23px;font-weight:700}
.banner .upto{color:#f6a21a;font-size:14px;font-weight:500;margin-top:4px}
.banner .off{color:#f7e21b;font-size:27px;font-weight:900;line-height:30px}
.banner p{font-size:8.4px;line-height:14.6px;margin-top:6px}
.btn{display:inline-flex;align-items:center;justify-content:center;color:var(--white);font-size:9px;font-weight:700;border-radius:2px;letter-spacing:.2px}
.banner .btn{background:var(--red);width:107px;height:24px;margin-top:8px}

.secbar{left:211px;top:399px;width:590px;height:33px;background:linear-gradient(#f3f3f3,#dcdcdc);border-bottom:2px solid #cfcfcf;font-size:12px;font-weight:700;padding:10px 0 0 25px;border-radius:4px 4px 0 0}
.count{left:211px;top:444px;font-size:16px;color:#777}
.count b{color:#555}
.select{top:441px;height:22px;border:1px solid #ddd;font-size:11px;color:#999;padding:4px 0 0 7px}
.select span{color:#333}
.select svg{position:absolute;right:5px;top:7px}

.product{width:171px}
.product .thumb{width:171px;height:171px;border:1px solid #c8c8c8;border-radius:4px;padding:14px}
.product .thumb div{width:100%;height:100%;border-radius:50%}
.product .price{margin-top:11px;color:var(--red);font-size:13px;font-weight:700}
.product h3{font-size:11px;font-weight:700;margin-top:3px}
.product p{font-size:9.5px;line-height:13px;color:#333;margin-top:4px}
.qty{display:flex;align-items:center;gap:6px;font-size:8.5px;font-weight:700;margin-top:6px}
.qty i{font-style:normal;width:16px;height:15px;border:1px solid #ddd;color:#aaa;font-weight:400;text-align:center;line-height:14px}
.qty em{font-style:normal;color:#bbb;font-weight:400}
.actions{display:flex;justify-content:space-between;margin-top:11px}
.actions .btn{width:82px;height:24px}
.add{background:var(--red)}
.view{background:#555}

.footer{left:0;top:1208px;width:844px;height:248px;background:var(--footer);font-size:10.5px;color:#333}
.footer ul{list-style:none}
.footer li{line-height:18.4px}
.vline{width:1px;background:#555;top:13px;height:154px}
.badge{width:107px;height:36px;border:2px solid #111;border-radius:4px;display:flex;align-items:center;gap:10px;padding-left:10px}
.badge.dark{background:#111}
.social{width:28px;height:28px;border-radius:50%;background:#111;top:17px}
.card{height:22px;border-radius:2px;background:#222;top:186px}
</style>
</head>
<body>
<div class="stage">
 <div class="page">
  <div class="abs topbar">
   <div class="abs phone">
    <svg width="12" height="12" viewBox="0 0 24 24"><path d="M6.6 10.8a15 15 0 0 0 6.6 6.6l2.2-2.2c.3-.3.7-.4 1-.2 1.1.4 2.3.6 3.6.6.6 0 1 .4 1 1V20c0 .6-.4 1-1 1A17 17 0 0 1 3 4c0-.6.4-1 1-1h3.5c.6 0 1 .4 1 1 0 1.3.2 2.5.6 3.6.1.3 0 .7-.2 1z" fill="none" stroke="#555" stroke-width="1.6"/></svg>
    1300 555 019
   </div>
   <nav class="abs"><span>Products</span><span>Login</span><span>Register</span><span>My Wishlist</span><span>My Cart</span></nav>
  </div>

  <header class="abs header">
   <div class="abs brand"><span>BROVAN MARKET</span><span class="dot"></span></div>
   <div class="abs search">
    <input value="Search" readonly>
    <button aria-label="Search"><svg width="13" height="13" viewBox="0 0 16 16"><circle cx="6.5" cy="6.5" r="4.8" fill="none" stroke="#fff" stroke-width="2"/><path d="M10 10l4.5 4.5" stroke="#fff" stroke-width="2.2"/></svg></button>
   </div>
   <div class="abs cart">YOUR CART
    <svg width="50" height="38" viewBox="0 0 50 38">
     <path d="M14 8h26l-4 14H18z" fill="none" stroke="var(--blue)" stroke-width="3"/>
     <path d="M40 8l3-6h6M18 22l-2 6h22" fill="none" stroke="var(--blue)" stroke-width="3"/>
     <path d="M20 13h16M21 17h13" stroke="var(--blue)" stroke-width="2"/>
     <circle cx="20" cy="33" r="3" fill="var(--blue)"/><circle cx="34" cy="33" r="3" fill="var(--blue)"/>
     <circle cx="7" cy="7" r="7" fill="var(--blue)"/><text x="7" y="10.5" font-size="10" fill="#fff" text-anchor="middle" font-family="Roboto,sans-serif">1</text>
    </svg>
   </div>
  </header>

  <aside class="abs cats">
   <h2>CATAGORIES</h2>
   <ul>
    <li>Baby</li><li class="active">Bakery</li><li>Baking Needs</li><li>Beverages</li><li>Biscuits</li><li>Breakfast Foods</li><li>Canned Food</li><li>Cheese</li><li>Chilled Foods</li><li>Chips</li><li>Condiments</li><li>Confectionary</li><li>Cooking Needs</li><li>Deserts</li>
   </ul>
  </aside>

  <section class="abs banner">
   <div class="shade" role="img" aria-label="Photograph of fresh vegetables on a dark background"></div>
   <div class="copy">
    <h1>Featured Product</h1>
    <div class="upto">GET UPTO</div>
    <div class="off">10% OFF</div>
    <p>Lorem ipsum dolor sit amet, consectetuer adipiscing elit, sed diam nonummy nibh euismod tincidunt ut laoreet dolore magna aliquam erat volutpat. Ut wisi enim ad minim veniam, quis nostrud exerci tation ullamcorper suscipit lobortis nisl ut aliquip ex ea commodo consequat.</p>
    <span class="btn">SHOP NOW!</span>
   </div>
  </section>

  <div class="abs secbar">FEATURED PRODUCT</div>
  <div class="abs count">Showing <b>38</b> products</div>
  <div class="abs select" style="left:538px;width:100px">Sort By: <span>Price</span>
   <svg width="8" height="6" viewBox="0 0 8 6"><path d="M1 1l3 3 3-3" fill="none" stroke="#999"/></svg></div>
  <div class="abs select" style="left:649px;width:136px">Filter By: <span>Homebrand</span>
   <svg width="8" height="6" viewBox="0 0 8 6"><path d="M1 1l3 3 3-3" fill="none" stroke="#999"/></svg></div>

  <!-- product grid -->
  <article class="abs product" style="left:211px;top:482px">
   <div class="thumb"><div role="img" aria-label="Photo of a bag of red apples" style="background:radial-gradient(circle,#c8192a 0%,#e04050 45%,#fff 72%)"></div></div>
   <div class="price">$8.39</div><h3>Apples Red 2kg Bag</h3>
   <p>Lorem ipsum dolor sit amet, consect etuer adipiscing elit, sed diam nonu mmy nibh euismod tincidunt ut laoreet dolore magna aliquam erat volutpat.</p>
   <div class="qty">QUANTITY <i>1</i><em>Apply</em></div>
   <div class="actions"><span class="btn add">ADD TO CART</span><span class="btn view">VIEW DETAILS</span></div>
  </article>
  <article class="abs product" style="left:420px;top:482px">
   <div class="thumb"><div role="img" aria-label="Photo of a single red apple" style="background:radial-gradient(circle,#b8303a 0%,#d77a6a 35%,#fff 55%)"></div></div>
   <div class="price">$0.60</div><h3>Apples Red 2kg Bag</h3>
   <p>Lorem ipsum dolor sit amet, consect etuer adipiscing elit, sed diam nonu mmy nibh euismod tincidunt ut laoreet dolore magna aliquam erat volutpat.</p>
   <div class="qty">QUANTITY <i>1</i><em>Apply</em></div>
   <div class="actions"><span class="btn add">ADD TO CART</span><span class="btn view">VIEW DETAILS</span></div>
  </article>
  <article class="abs product" style="left:629px;top:482px">
   <div class="thumb"><div role="img" aria-label="Photo of a green apple" style="background:radial-gradient(circle,#6cc02a 0%,#4ea320 35%,#fff 56%)"></div></div>
   <div class="price">$0.60</div><h3>Apples Red 2kg Bag</h3>
   <p>Lorem ipsum dolor sit amet, consect etuer adipiscing elit, sed diam nonu mmy nibh euismod tincidunt ut laoreet dolore magna aliquam erat volutpat.</p>
   <div class="qty">QUANTITY <i>1</i><em>Apply</em></div>
   <div class="actions"><span class="btn add">ADD TO CART</span><span class="btn view">VIEW DETAILS</span></div>
  </article>

  <article class="abs product" style="left:211px;top:842px">
   <div class="thumb"><div role="img" aria-label="Photo of a single deep red apple" style="background:radial-gradient(circle,#c8152f 0%,#d52a40 30%,#fff 50%)"></div></div>
   <div class="price">$0.60</div><h3>Apples Red 2kg Bag</h3>
   <p>Lorem ipsum dolor sit amet, consect etuer adipiscing elit, sed diam nonu mmy nibh euismod tincidunt ut laoreet dolore magna aliquam erat volutpat.</p>
   <div class="qty">QUANTITY <i>1</i><em>Apply</em></div>
   <div class="actions"><span class="btn add">ADD TO CART</span><span class="btn view">VIEW DETAILS</span></div>
  </article>
  <article class="abs product" style="left:420px;top:842px">
   <div class="thumb"><div role="img" aria-label="Photo of a red and yellow apple" style="background:radial-gradient(circle,#e8a040 0%,#d86040 30%,#fff 50%)"></div></div>
   <div class="price">$0.60</div><h3>Apples Red 2kg Bag</h3>
   <p>Lorem ipsum dolor sit amet, consect etuer adipiscing elit, sed diam nonu mmy nibh euismod tincidunt ut laoreet dolore magna aliquam erat volutpat.</p>
   <div class="qty">QUANTITY <i>1</i><em>Apply</em></div>
   <div class="actions"><span class="btn add">ADD TO CART</span><span class="btn view">VIEW DETAILS</span></div>
  </article>
  <article class="abs product" style="left:629px;top:842px">
   <div class="thumb"><div role="img" aria-label="Photo of a pile of green apples" style="background:radial-gradient(circle,#b8d23a 0%,#c6db5a 40%,#fff 68%)"></div></div>
   <div class="price">$5.20</div><h3>Apples Red 2kg Bag</h3>
   <p>Lorem ipsum dolor sit amet, consect etuer adipiscing elit, sed diam nonu mmy nibh euismod tincidunt ut laoreet dolore magna aliquam erat volutpat.</p>
   <div class="qty">QUANTITY <i>1</i><em>Apply</em></div>
   <div class="actions"><span class="btn add">ADD TO CART</span><span class="btn view">VIEW DETAILS</span></div>
  </article>

  <footer class="abs footer">
   <div class="abs" style="left:42px;top:14px">Download Our App</div>
   <div class="abs badge dark" style="left:42px;top:46px" role="img" aria-label="App store download badge"></div>
   <div class="abs badge" style="left:42px;top:84px">
    <svg width="14" height="24" viewBox="0 0 14 24"><rect x="1" y="1" width="12" height="22" rx="2" fill="none" stroke="#111" stroke-width="2"/></svg>
    <span style="font-size:11.5px;line-height:11px">Mobile site<br>Available</span>
   </div>
   <div class="abs" style="left:42px;top:152px">We accept</div>
   <div class="abs card" style="left:43px;width:34px"></div>
   <div class="abs card" style="left:85px;width:35px"></div>
   <div class="abs" style="left:130px;top:184px;width:26px;height:26px;border-radius:50%;background:#c9a43a;border:2px solid #222"></div>
   <div class="abs" style="left:74px;top:227px">© Tallow Pty Ltd 2014 - All Rights Reserved <small style="font-size:6px">ver 1.1.2</small></div>

   <ul class="abs" style="left:235px;top:12px"><li>My Account</li><li>My Past Orders</li><li>Online Specials</li><li>Everyday Specials</li></ul>
   <ul class="abs" style="left:235px;top:129px"><li>About Tallow</li><li>About Us</li></ul>
   <div class="abs vline" style="left:342px"></div>
   <ul class="abs" style="left:365px;top:12px"><li>Delivery</li><li>FAQ</li><li>Privacy Policy</li><li>Terms &amp; Conditions</li></ul>
   <ul class="abs" style="left:365px;top:129px"><li>Contact us</li><li>1300 555 019</li></ul>
   <div class="abs vline" style="left:471px"></div>
   <div class="abs" style="left:493px;top:13px;line-height:16px">End User License<br>Agreement</div>
   <div class="abs social" style="left:625px" aria-label="Social link"></div>
   <div class="abs social" style="left:668px" aria-label="Social link"></div>
   <div class="abs social" style="left:710px" aria-label="Social link"></div>
  </footer>
 </div>
</div>
</body>
</html>
```